Business Card for Ferncliff Massage

I need a business card for my massage therapy & cannabis oil practice. I already have a logo,the "massage" got edited out of this file. I will send the original soon. I need these elements to be on the card:
web: FerncliffMassage.example
ph: 541/382-9147
email: Marla.Quintavelle@mailbox.example
Other slogans, statements to consider:
Science Geek, Massage Therapist, Neuromuscular Therapy, Cannabis Spa Treatments, Raindrop Therapy, Essential Oils
Target Market(s)
women between 20 & 65, people with enough $ to afford regular massage, people who recently had a motor vehicle accident, Halvora HMC insured
Industry/Entity Type
Massage Therapy
Contact Information for Business Card
I would like to see my bear logo featured; contact details, greens & blues preferred colors.

```html
<!DOCTYPE html>
<html lang="en">
<head>
<meta charset="utf-8">
<title>Ferncliff Massage – Business Card</title>
<link rel="stylesheet" href="https://fonts.googleapis.com/css2?family=Cinzel:wght@400&family=Federo&display=swap">
<style>
  :root {
    --page-bg: #e9e7e3;
    --navy: #054b6e;
    --teal: #047a7e;
    --mid-blue: #1479a8;
    --sky: #0a8fcc;
    --leaf: #0b6b2a;
    --brand-green: #3d8a3e;
    --mist: #cfe8ea;
  }
  * { box-sizing: border-box; margin: 0; padding: 0; }
  html, body { width: 1200px; height: 1200px; overflow: hidden; background: var(--page-bg); }
  .canvas { position: relative; width: 1200px; height: 1200px; }

  .card {
    position: absolute;
    left: 210px;
    width: 780px;
    height: 445px;
    background: var(--navy);
    overflow: hidden;
  }
  .card--front { top: 140px; }
  .card--back { top: 650px; }

  .front-arcs { position: absolute; inset: 0; }

  .brand {
    position: absolute;
    left: 40px;
    top: 285px;
    display: flex;
    align-items: center;
    gap: 12px;
  }
  .brand__dot {
    width: 16px; height: 16px;
    border-radius: 50%;
    background: var(--brand-green);
  }
  .brand__name {
    font-family: "Federo", sans-serif;
    font-size: 52px;
    color: var(--brand-green);
    line-height: 1;
  }

  .contacts {
    position: absolute;
    right: 30px;
    top: 155px;
    display: flex;
    flex-direction: column;
    align-items: flex-end;
    gap: 6px;
  }
  .contact {
    display: flex;
    align-items: center;
    gap: 10px;
    color: var(--leaf);
  }
  .contact__text { font-family: "Cinzel", serif; font-size: 19px; }
  .contact--phone .contact__text { font-family: "Federo", sans-serif; font-size: 34px; }
  .contact__icon { width: 48px; height: 48px; flex: none; }

  .services {
    position: absolute;
    left: 0; right: 0;
    top: 155px;
    height: 155px;
    background: var(--teal);
    display: flex;
    flex-direction: column;
    justify-content: center;
    align-items: center;
    gap: 8px;
    list-style: none;
    font-family: "Cinzel", serif;
    font-size: 22px;
    color: var(--mist);
    line-height: 1.2;
  }
</style>
</head>
<body>
<main class="canvas">
  <section class="card card--front">
    <svg class="front-arcs" width="780" height="445" viewBox="0 0 780 445" aria-hidden="true">
      <circle cx="660" cy="230" r="395" fill="var(--teal)"/>
      <circle cx="660" cy="230" r="355" fill="var(--mid-blue)"/>
      <circle cx="660" cy="230" r="325" fill="var(--sky)"/>
    </svg>

    <div class="brand">
      <span class="brand__dot"></span>
      <span class="brand__name">Ferncliff</span>
    </div>

    <div class="contacts">
      <div class="contact contact--phone">
        <span class="contact__text">541/382-9147</span>
        <svg class="contact__icon" viewBox="0 0 48 48" aria-hidden="true">
          <circle cx="24" cy="24" r="21" fill="none" stroke="var(--leaf)" stroke-width="2.5"/>
          <path d="M17 13 l5 0 l2 6 l-3 2 q2 5 7 7 l2-3 l6 2 l0 5 q-2 2 -5 1 q-12 -4 -15 -15 q-1 -3 1 -5z" fill="var(--leaf)"/>
        </svg>
      </div>
      <div class="contact">
        <span class="contact__text">Marla.Quintavelle@mailbox.example</span>
        <svg class="contact__icon" viewBox="0 0 48 48" aria-hidden="true">
          <circle cx="24" cy="24" r="21" fill="none" stroke="var(--leaf)" stroke-width="2.5"/>
          <rect x="13" y="17" width="22" height="15" fill="var(--leaf)"/>
          <path d="M13 17 L24 26 L35 17" fill="none" stroke="var(--sky)" stroke-width="1.8"/>
        </svg>
      </div>
      <div class="contact">
        <span class="contact__text">FerncliffMassage.example</span>
        <svg class="contact__icon" viewBox="0 0 48 48" aria-hidden="true">
          <circle cx="24" cy="24" r="21" fill="none" stroke="var(--leaf)" stroke-width="2.5"/>
          <rect x="17" y="15" width="14" height="20" rx="7" fill="var(--leaf)"/>
          <line x1="24" y1="15" x2="24" y2="23" stroke="var(--sky)" stroke-width="1.6"/>
          <line x1="17" y1="23" x2="31" y2="23" stroke="var(--sky)" stroke-width="1.6"/>
        </svg>
      </div>
    </div>
  </section>

  <section class="card card--back">
    <ul class="services">
      <li>Science Geek · Massage Therapist</li>
      <li>Neuromuscular Therapy</li>
      <li>Cannabis Spa Treatments</li>
      <li>Raindrop Therapy · Essential Oils</li>
    </ul>
  </section>
</main>
</body>
</html>
```